Fernvale Build for Rent Development Company

We are a new multifamily, build for rent, development company that is looking to build a pitch book outlining our company along with the real estate opportunity. We would want the style to be a modern, clean aesthetic with cool colors

```html
<!DOCTYPE html>
<html lang="en">
<head>
<meta charset="utf-8">
<title>Fernvale Pitch Book</title>
<link href="https://fonts.googleapis.com/css2?family=Fira+Sans:wght@400;500;600;700&display=swap" rel="stylesheet">
<style>
:root{
  --navy:#131f2e;
  --slate:#5d7a8e;
  --gray:#9da1a5;
  --light:#e7e9eb;
  --paper:#ffffff;
  --ink:#1b2633;
  --muted:#7b828a;
}
*{margin:0;padding:0;box-sizing:border-box}
html,body{width:765px;height:1200px;overflow:hidden;background:#fff}
body{position:relative;font-family:"Fira Sans",sans-serif;color:var(--ink)}
.slide{position:absolute;width:245px;height:138px;overflow:hidden;background:var(--paper);box-shadow:0 1px 3px rgba(0,0,0,.25)}
.slide *{position:absolute}
.navy{background:var(--navy)}
.ph{background:linear-gradient(160deg,#8e9aa6,#4d5964)}
.ph.sky{background:linear-gradient(160deg,#cfdbe6,#6f8597)}
.ph.warm{background:linear-gradient(160deg,#9a8674,#3e3530)}
.ph.crowd{background:linear-gradient(160deg,#7d6a5e,#2d2a2e)}
.ph.plant{background:linear-gradient(160deg,#b7bcc0,#5f666d)}
.title{font-weight:700;font-size:9.5px;white-space:nowrap}
.bracket{width:9px;height:13px;border-top:1.5px solid var(--gray);border-left:1.5px solid var(--gray)}
.tiny{font-size:2.8px;line-height:1.45;color:var(--muted)}
.w{color:#fff}
.wt{color:#c9cfd5}
.logo{font-size:7px;font-weight:600;letter-spacing:.3px;white-space:nowrap}
.pnum{font-size:2.6px;right:10px;bottom:6px}
.menu{right:10px;top:6px;width:6px;height:2px;border-top:.6px solid var(--gray);border-bottom:.6px solid var(--gray)}
.stat{font-weight:700;font-size:8px}
.tile{width:55px;height:27px;display:flex;align-items:center;font-size:4.2px;color:#fff;padding-left:20px}
.tile i{left:7px;top:9px;width:8px;height:8px;border:.7px solid #fff;border-radius:1px}
.pill{height:5px;border-radius:3px;background:#fff;font-size:2.2px;color:var(--ink);display:flex;align-items:center;justify-content:center;width:22px}
.btn{font-size:2.4px;letter-spacing:.4px;color:#fff;display:flex;align-items:center;justify-content:center}
</style>
</head>
<body>

<!-- Row 1 -->
<section class="slide navy" style="left:8px;top:16px">
  <div style="left:13px;top:0;width:104px;height:114px;background:var(--light)"></div>
  <div style="left:13px;top:114px;width:104px;height:18px;background:var(--gray)"></div>
  <div class="ph warm" role="img" aria-label="Restaurant interior photo" style="left:117px;top:19px;width:128px;height:95px"></div>
  <div class="tiny w" style="right:12px;top:6px;font-size:2.6px">www.fernvaledb.com</div>
  <div class="title" style="left:27px;top:19px;font-size:11.5px;line-height:1.3;color:var(--navy);white-space:normal;width:84px">Providing unique solutions for every industry.</div>
  <div class="tiny" style="left:28px;top:86px;width:72px;color:#7d9bb0">We plan, build and manage rental homes for every kind of community.</div>
  <div class="pill" style="left:152px;top:98px">Banking</div>
  <div class="pill" style="left:176px;top:98px">Health</div>
  <div class="pill" style="left:200px;top:98px">Hospitality</div>
  <div class="pill" style="left:144px;top:105px">Industrial</div>
  <div class="pill" style="left:168px;top:105px">Professional</div>
  <div class="pill" style="left:192px;top:105px">Retail</div>
  <div class="pill" style="left:216px;top:105px">Architecture</div>
  <div style="left:29px;top:122px;width:4px;height:4px;border-radius:50%;background:var(--navy)"></div>
  <div style="left:35px;top:122px;width:4px;height:4px;border-radius:50%;background:var(--navy)"></div>
  <div style="left:41px;top:122px;width:4px;height:4px;border-radius:50%;background:var(--navy)"></div>
  <div style="left:47px;top:122px;width:4px;height:4px;border-radius:50%;background:var(--navy)"></div>
  <div class="logo w" style="right:12px;top:123px">Fernvale</div>
</section>

<section class="slide" style="left:259px;top:16px">
  <div class="ph sky" role="img" aria-label="Glass office tower photo" style="left:0;top:0;width:123px;height:114px"></div>
  <div style="left:0;top:114px;width:64px;height:24px;background:var(--gray)"></div>
  <div style="left:64px;top:114px;width:59px;height:24px;background:#6c7178"></div>
  <div class="w" style="left:11px;top:119px;font-size:3.6px;font-weight:600">Presented by.<br><span style="position:static;font-size:2.2px;font-weight:400">Agency Name</span></div>
  <div class="w" style="left:74px;top:122px;font-size:3.6px;font-weight:600">Presented by.<br><span style="position:static;font-size:2.2px;font-weight:400">Agency Name</span></div>
  <div class="navy" style="left:123px;top:38px;width:122px;height:100px"></div>
  <div class="logo" style="right:13px;top:17px;font-size:9px;color:var(--navy)">Fernvale</div>
  <div class="title w" style="right:21px;top:58px;font-size:11px;line-height:1.35;text-align:right;white-space:normal;width:86px">Providing unique solutions for every industry.</div>
</section>

<section class="slide navy" style="left:511px;top:16px">
  <div style="left:138px;top:55px;width:107px;height:83px;background:var(--gray)"></div>
  <div style="left:186px;top:0;width:59px;height:12px;background:#fff"></div>
  <div class="ph sky" role="img" aria-label="Tower facade photo" style="left:138px;top:12px;width:107px;height:84px;background:linear-gradient(160deg,#e5e7e9,#55595e)"></div>
  <div class="logo w" style="left:12px;top:20px;font-size:10px">Fernvale</div>
  <div class="title w" style="left:12px;top:53px;font-size:11px;line-height:1.35;white-space:normal;width:110px">Providing unique solutions for every industry.</div>
  <div class="tiny wt" style="left:12px;top:109px;width:90px">We plan, build and manage rental homes for every kind of community.</div>
  <div class="w" style="left:151px;top:108px;font-size:3.6px;font-weight:600">Presented by.<br><span style="position:static;font-size:2.2px;font-weight:400">Agency Name</span></div>
  <div class="w" style="left:200px;top:108px;font-size:3.6px;font-weight:600">Excelusive To.<br><span style="position:static;font-size:2.2px;font-weight:400">Client Name</span></div>
</section>

<!-- Row 2 -->
<section class="slide navy" style="left:8px;top:188px">
  <div class="ph warm" role="img" aria-label="Dining hall interior photo" style="left:0;top:0;width:60px;height:138px;background:linear-gradient(160deg,#8a8580,#3a3835)"></div>
  <div class="bracket" style="left:61px;top:0"></div>
  <div class="title w" style="left:71px;top:6px">Table of Content</div>
  <div style="left:78px;top:31px;width:160px;border-top:.4px solid #3a4656"></div>
  <div style="left:78px;top:56px;width:160px;border-top:.4px solid #3a4656"></div>
  <div style="left:78px;top:81px;width:160px;border-top:.4px solid #3a4656"></div>
  <div style="left:78px;top:106px;width:160px;border-top:.4px solid #3a4656"></div>
  <div class="w" style="left:82px;top:40px;font-size:3.5px">Page</div><div class="stat w" style="left:100px;top:38px;font-size:10px">01.</div>
  <div class="tiny wt" style="left:135px;top:39px;width:95px">Overview of the company, its mission and the people leading it.</div>
  <div class="w" style="left:82px;top:65px;font-size:3.5px">Page</div><div class="stat w" style="left:100px;top:63px;font-size:10px">02.</div>
  <div class="tiny wt" style="left:135px;top:64px;width:95px">The build for rent model and the market we are focused on.</div>
  <div class="w" style="left:82px;top:89px;font-size:3.5px">Page</div><div class="stat w" style="left:100px;top:87px;font-size:10px">03.</div>
  <div class="tiny wt" style="left:135px;top:88px;width:95px">Current projects, pipeline and delivery timeline in detail.</div>
  <div class="w" style="left:82px;top:114px;font-size:3.5px">Page</div><div class="stat w" style="left:100px;top:112px;font-size:10px">04.</div>
  <div class="tiny wt" style="left:135px;top:113px;width:95px">Financial summary, returns and the investment opportunity.</div>
  <div class="pnum w">4</div>
</section>

<section class="slide" style="left:259px;top:188px">
  <div class="ph crowd" role="img" aria-label="Team group photo" style="left:0;top:0;width:109px;height:138px"></div>
  <div class="menu"></div>
  <div class="bracket" style="left:123px;top:20px"></div>
  <div class="title" style="left:133px;top:26px">About Us</div>
  <div class="tiny" style="left:133px;top:48px;width:102px;font-size:3px;color:#4a525b">Fernvale has created a unique family environment where we work as a team to achieve success through design and construction for our clients. We are dedicated to customer service and creating a friendly place for employees and clients to work and thrive together. Everyone works together to help each other establish great relationships and deliver unique projects. We also take pride in providing company offered activities that offer the opportunity to get to know each other and grow together. We are more than just a job; we are part of your life.</div>
  <div class="btn navy" style="left:131px;top:101px;width:40px;height:10px">CONSULT WITH US</div>
  <div class="pnum">5</div>
</section>

<section class="slide" style="left:511px;top:188px">
  <div class="ph" role="img" aria-label="Portrait of smiling team member" style="left:0;top:0;width:109px;height:138px;background:linear-gradient(160deg,#c8c4c0,#7c6e9e)"></div>
  <div class="menu"></div>
  <div class="bracket" style="left:123px;top:20px"></div>
  <div class="title" style="left:133px;top:26px;font-size:9.5px;line-height:1.15;white-space:normal;width:108px">Assisting our client's growth through trust and relationships.</div>
  <div class="tile navy" style="left:65px;top:65px"><i></i>Professional</div>
  <div class="tile" style="left:123px;top:65px;background:var(--gray)"><i></i>Banking</div>
  <div class="tile" style="left:181px;top:65px;background:#7c8287"><i></i>Hospitality</div>
  <div class="tile" style="left:65px;top:95px;background:var(--slate)"><i></i>Retail</div>
  <div class="tile" style="left:123px;top:95px;background:#a8b6c0"><i></i>Health</div>
  <div class="tile navy" style="left:181px;top:95px"><i></i>Industrial</div>
  <div class="pnum">6</div>
</section>

<!-- Row 3 -->
<section class="slide navy" style="left:8px;top:359px">
  <div class="ph warm" role="img" aria-label="Cafe interior photo" style="left:13px;top:15px;width:51px;height:54px"></div>
  <div class="bracket" style="left:75px;top:15px"></div>
  <div class="title w" style="left:85px;top:22px">Your Title Goes Here</div>
  <div class="pill" style="left:17px;top:78px;width:27px;background:none;border:.4px solid #566271;color:#8a96a4">Years Experience</div>
  <div class="pill" style="left:68px;top:78px;width:27px;background:none;border:.4px solid #566271;color:#8a96a4">Case Every Years</div>
  <div class="pill" style="left:117px;top:78px;width:27px;background:none;border:.4px solid #566271;color:#8a96a4">Rating Clients</div>
  <div class="stat w" style="left:17px;top:89px">30+</div>
  <div class="stat w" style="left:68px;top:89px">130K</div>
  <div class="stat w" style="left:117px;top:89px">4.9</div>
  <div class="tiny wt" style="left:18px;top:103px;width:38px">Homes delivered across many growing regions</div>
  <div class="tiny wt" style="left:69px;top:103px;width:38px">Square feet built for renters each year</div>
  <div class="tiny wt" style="left:118px;top:103px;width:38px">Average rating from our resident families</div>
  <div style="left:61px;top:76px;height:38px;border-left:.4px solid #3a4656"></div>
  <div style="left:111px;top:76px;height:38px;border-left:.4px solid #3a4656"></div>
  <div class="ph warm" role="img" aria-label="Restaurant seating photo" style="left:163px;top:74px;width:64px;height:64px"></div>
  <div class="logo w" style="left:13px;top:126px;font-size:6px">Fernvale</div>
  <div class="pnum w">7</div>
</section>

<section class="slide" style="left:259px;top:359px">
  <div class="bracket" style="left:0;top:0"></div>
  <div class="title" style="left:10px;top:6px">Your Title Goes Here</div>
  <div class="tiny" style="left:12px;top:24px;width:92px;font-size:3px">We build purpose designed rental communities that give residents space, comfort and quality at a fair monthly price.</div>
  <div class="tiny" style="left:129px;top:24px;width:95px;font-size:3px">Each project pairs efficient design with durable materials so investors see steady returns over the long term.</div>
  <div class="ph sky" role="img" aria-label="Glass tower looking up photo" style="left:11px;top:56px;width:83px;height:82px"></div>
  <div class="navy" style="left:94px;top:56px;width:151px;height:82px"></div>
  <div class="tiny wt" style="left:105px;top:68px;width:128px;font-size:3px">Our pipeline spans suburban markets with strong job growth, rising household formation and limited new rental supply.</div>
  <div class="stat" style="left:106px;top:97px;color:#7d9bb0">34K+</div>
  <div class="stat" style="left:146px;top:97px;color:#7d9bb0">625</div>
  <div class="stat" style="left:187px;top:97px;color:#7d9bb0">35+</div>
  <div class="tiny wt" style="left:106px;top:113px">Properties Sold</div>
  <div class="tiny wt" style="left:146px;top:113px">Project Completed</div>
  <div class="tiny wt" style="left:187px;top:113px">Satisfied Client</div>
</section>

<section class="slide" style="left:511px;top:359px">
  <div class="ph plant" role="img" aria-label="Factory floor photo" style="left:0;top:0;width:245px;height:84px"></div>
  <div class="tile" style="left:179px;top:16px;background:#fff;color:var(--ink);height:26px"><i style="border-color:var(--ink)"></i>Hospitality</div>
  <div class="tile" style="left:179px;top:45px;background:var(--light);color:var(--ink);height:26px"><i style="border-color:var(--ink)"></i>Industrial</div>
  <div class="bracket" style="left:12px;top:88px"></div>
  <div class="title" style="left:22px;top:94px">Your Title Goes Here</div>
  <div class="tiny" style="left:131px;top:97px;width:100px;font-size:3px">Modern industrial and hospitality sites near our communities support long term rental demand and resident jobs.</div>
  <div class="logo" style="left:15px;top:127px;font-size:6px;color:var(--navy)">Fernvale</div>
  <div class="pnum">9</div>
</section>

<!-- Row 4 -->
<section class="slide" style="left:8px;top:530px">
  <div class="bracket" style="left:0;top:0"></div>
  <div class="title" style="left:10px;top:6px">Your Title Goes Here</div>
  <div class="tiny" style="left:12px;top:24px;width:95px;font-size:3px">Every property is chosen for access to schools, transit and jobs so residents stay longer and vacancy stays low.</div>
  <div class="ph sky" role="img" aria-label="Modern branch building photo" style="left:125px;top:0;width:120px;height:69px;background:linear-gradient(170deg,#c6d3df,#4a5a66)"></div>
  <div class="navy" style="left:0;top:69px;width:245px;height:69px"></div>
  <div style="left:22px;top:77px;width:12px;height:12px;border-radius:50%;background:#d6dade"></div>
  <div style="left:98px;top:77px;width:12px;height:12px;border-radius:50%;background:#d6dade"></div>
  <div style="left:173px;top:77px;width:12px;height:12px;border-radius:50%;background:#d6dade"></div>
  <div style="left:91px;top:76px;height:44px;border-left:.4px solid #3a4656"></div>
  <div style="left:166px;top:76px;height:44px;border-left:.4px solid #3a4656"></div>
  <div class="w" style="left:22px;top:96px;font-size:3.8px;font-weight:600;line-height:1.25;width:60px">The Real Estate Market Today – Current trends and future projections</div>
  <div class="w" style="left:98px;top:96px;font-size:3.8px;font-weight:600;line-height:1.25;width:60px">Building Dreams, One Property at a Time</div>
  <div class="w" style="left:173px;top:96px;font-size:3.8px;font-weight:600;line-height:1.25;width:60px">Smart homes, sustainability, and urban living</div>
  <div class="tiny wt" style="left:22px;top:114px;width:62px">Demand for quality rentals keeps rising each year</div>
  <div class="tiny wt" style="left:98px;top:114px;width:62px">We guide each site from plan to lease up</div>
  <div class="tiny wt" style="left:173px;top:114px;width:62px">Efficient homes designed for modern renters</div>
  <div class="pnum w">10</div>
</section>

<section class="slide" style="left:259px;top:530px">
  <div class="ph" role="img" aria-label="Commercial building entrance photo" style="left:0;top:0;width:123px;height:138px;background:linear-gradient(180deg,#c9d2da 0,#7b8794 35%,#1d2226 60%,#d0d5d9)"></div>
  <div class="navy" style="left:123px;top:0;width:122px;height:77px"></div>
  <div class="bracket" style="left:141px;top:26px"></div>
  <div class="title w" style="left:151px;top:32px;line-height:1.15">Your Title<br>Goes Here</div>
  <div class="stat" style="left:140px;top:88px;font-size:7px">96%</div>
  <div class="tiny" style="left:169px;top:88px;width:60px">Of our homes are leased within the first months of opening</div>
  <div style="left:140px;top:103px;width:90px;border-top:.4px solid #c5c9cd"></div>
  <div class="stat" style="left:140px;top:110px;font-size:7px">179K</div>
  <div class="tiny" style="left:169px;top:110px;width:60px">Residents now call a Fernvale community their home</div>
  <div class="pnum">11</div>
</section>

<section class="slide navy" style="left:511px;top:530px">
  <div class="menu"></div>
  <div class="bracket" style="left:0;top:0"></div>
  <div class="title w" style="left:10px;top:6px">Our Clients</div>
  <div style="left:17px;top:53px;width:79px;height:66px;background:var(--slate)"></div>
  <div class="ph" role="img" aria-label="Client portrait photo" style="left:100px;top:46px;width:80px;height:73px;background:linear-gradient(160deg,#a9b4bc,#5b6670)"></div>
  <div style="left:184px;top:53px;width:61px;height:66px;background:#6a747c"></div>
  <div class="w" style="left:25px;top:60px;width:64px;font-size:3.2px;font-style:italic;line-height:1.6">I have been using Fernvale for over a year now and I love it! I can't imagine life without it. It's so easy to use, and the customer service is great.</div>
  <div class="w" style="left:192px;top:60px;width:50px;font-size:3.2px;font-style:italic;line-height:1.6">Fernvale makes me more productive and gets the job done in a fraction of the time</div>
  <div style="left:24px;top:103px;width:7px;height:7px;border-radius:50%;background:#c7cdd2"></div>
  <div class="w" style="left:37px;top:104px;font-size:2.6px">Marco Delane<br><span style="position:static;font-size:2px">Position here</span></div>
  <div style="left:108px;top:104px;width:7px;height:7px;border-radius:50%;background:#4c565f"></div>
  <div class="w" style="left:122px;top:105px;font-size:2.6px">Owen Castell<br><span style="position:static;font-size:2px">Position here</span></div>
  <div style="left:191px;top:104px;width:7px;height:7px;border-radius:50%;background:#c7cdd2"></div>
  <div class="w" style="left:204px;top:105px;font-size:2.6px">Lena Moray<br><span style="position:static;font-size:2px">Position here</span></div>
  <div style="left:0;top:119px;width:245px;height:19px;background:#fff"></div>
  <div class="logo" style="left:15px;top:127px;font-size:6px;color:var(--navy)">Fernvale</div>
  <div class="pnum">12</div>
</section>

<!-- Row 5 -->
<section class="slide" style="left:8px;top:701px">
  <div class="bracket" style="left:0;top:0"></div>
  <div class="title" style="left:10px;top:6px">Out Expert Team</div>
  <div class="ph" role="img" aria-label="Team member portrait" style="left:17px;top:35px;width:49px;height:37px"></div>
  <div style="left:66px;top:35px;width:49px;height:37px;background:var(--gray)"></div>
  <div class="ph" role="img" aria-label="Team member portrait" style="left:126px;top:35px;width:49px;height:37px;background:linear-gradient(160deg,#d9dcdf,#7d858c)"></div>
  <div class="navy" style="left:175px;top:35px;width:49px;height:37px"></div>
  <div class="ph" role="img" aria-label="Team member portrait" style="left:17px;top:77px;width:49px;height:37px;background:linear-gradient(160deg,#8a7e72,#d8d4d0)"></div>
  <div class="navy" style="left:66px;top:77px;width:49px;height:37px"></div>
  <div class="ph" role="img" aria-label="Team member portrait" style="left:126px;top:77px;width:49px;height:37px;background:linear-gradient(160deg,#c9c6c0,#8a8680)"></div>
  <div style="left:175px;top:77px;width:49px;height:37px;background:var(--gray)"></div>
  <div class="w" style="left:70px;top:41px;font-size:3.4px;font-weight:600">Name Team Here<br><span style="position:static;font-size:2px;font-weight:400">Position here</span></div>
  <div class="w" style="left:179px;top:41px;font-size:3.4px;font-weight:600">Name Team Here<br><span style="position:static;font-size:2px;font-weight:400">Position here</span></div>
  <div class="w" style="left:70px;top:83px;font-size:3.4px;font-weight:600">Name Team Here<br><span style="position:static;font-size:2px;font-weight:400">Position here</span></div>
  <div class="w" style="left:179px;top:83px;font-size:3.4px;font-weight:600">Name Team Here<br><span style="position:static;font-size:2px;font-weight:400">Position here</span></div>
  <div class="tiny w" style="left:70px;top:63px;font-size:2.2px">@accountname</div>
  <div class="tiny w" style="left:179px;top:63px;font-size:2.2px">@accountname</div>
  <div class="tiny w" style="left:70px;top:105px;font-size:2.2px">@accountname</div>
  <div class="tiny w" style="left:179px;top:105px;font-size:2.2px">@accountname</div>
  <div class="logo" style="left:15px;top:127px;font-size:6px;color:var(--navy)">Fernvale</div>
  <div class="pnum">13</div>
</section>

<section class="slide" style="left:259px;top:701px">
  <div class="bracket" style="left:0;top:0"></div>
  <div class="title" style="left:10px;top:6px">Our Process</div>
  <svg style="left:0;top:0" width="245" height="138" viewBox="0 0 245 138">
    <path d="M38 50 Q122 40 200 50" fill="none" stroke="#ccd0d4" stroke-width=".4" stroke-dasharray="1.5 1"/>
    <g stroke-width="3">
      <circle cx="47" cy="76" r="14" fill="#fff" stroke="var(--navy)"/>
      <circle cx="85" cy="76" r="14" fill="#eef0f2" stroke="var(--gray)"/>
      <circle cx="123" cy="76" r="14" fill="#eef0f2" stroke="#6f767d"/>
      <circle cx="161" cy="76" r="14" fill="#dfe6ec" stroke="var(--slate)"/>
      <circle cx="199" cy="76" r="14" fill="#fff" stroke="var(--navy)"/>
    </g>
    <g fill="none" stroke="#fff" stroke-width=".7">
      <circle cx="47" cy="76" r="8" fill="var(--navy)"/>
      <circle cx="199" cy="76" r="8" fill="var(--navy)"/>
    </g>
    <g fill="#fff" stroke="var(--navy)" stroke-width=".7">
      <circle cx="47" cy="57" r="2"/><circle cx="123" cy="57" r="2"/><circle cx="199" cy="57" r="2"/>
      <circle cx="85" cy="95" r="2" stroke="var(--gray)"/><circle cx="161" cy="95" r="2" stroke="var(--slate)"/>
    </g>
  </svg>
  <div style="left:20px;top:29px;width:54px;text-align:center;font-size:3.6px;font-weight:600">Heading Here<div class="tiny" style="position:static">A quiet step that keeps every phase on track</div></div>
  <div style="left:96px;top:29px;width:54px;text-align:center;font-size:3.6px;font-weight:600;color:var(--muted)">Heading Here<div class="tiny" style="position:static">A quiet step that keeps every phase on track</div></div>
  <div style="left:172px;top:29px;width:54px;text-align:center;font-size:3.6px;font-weight:600">Heading Here<div class="tiny" style="position:static">A quiet step that keeps every phase on track</div></div>
  <div style="left:58px;top:111px;width:54px;text-align:center;font-size:3.6px;font-weight:600;color:var(--gray)">Heading Here<div class="tiny" style="position:static">A quiet step that keeps every phase on track</div></div>
  <div style="left:134px;top:111px;width:54px;text-align:center;font-size:3.6px;font-weight:600;color:var(--slate)">Heading Here<div class="tiny" style="position:static">A quiet step that keeps every phase on track</div></div>
  <div class="logo" style="left:15px;top:127px;font-size:6px;color:var(--navy)">Fernvale</div>
  <div class="pnum">14</div>
</section>

<section class="slide" style="left:511px;top:701px">
  <div class="bracket" style="left:0;top:0"></div>
  <div class="title" style="left:10px;top:6px">Funnel Infographic</div>
  <svg style="left:0;top:0" width="245" height="138" viewBox="0 0 245 138">
    <ellipse cx="124" cy="28" rx="54" ry="5" fill="#cfd5da"/>
    <polygon points="70,28 178,28 172,38 76,38" fill="#4e5d6c"/>
    <polygon points="76,38 172,38 166,47 82,47" fill="#6f8090"/>
    <polygon points="82,47 166,47 160,56 88,56" fill="#5d6e7e"/>
    <polygon points="88,56 160,56 154,66 94,66" fill="#8fa3b4"/>
    <polygon points="94,66 154,66 148,75 100,75" fill="#b8c3cc"/>
    <polygon points="100,75 148,75 142,84 110,84" fill="#3b4756"/>
    <rect x="110" y="84" width="32" height="42" fill="#2d3845"/>
    <ellipse cx="126" cy="126" rx="16" ry="2" fill="#c4c9cd"/>
    <g stroke="#9aa1a8" stroke-width=".3" fill="none">
      <path d="M178 33 L195 36"/><path d="M172 42 L182 55"/><path d="M166 61 L170 75"/>
      <path d="M142 104 L160 104"/><path d="M70 43 L82 46"/><path d="M73 62 L86 60"/><path d="M85 82 L100 80"/>
    </g>
  </svg>
  <div class="w" style="left:116px;top:40px;font-size:2.3px">Heading 01</div>
  <div class="w" style="left:116px;top:49px;font-size:2.3px">Heading 02</div>
  <div class="w" style="left:116px;top:58px;font-size:2.3px">Heading 03</div>
  <div class="w" style="left:116px;top:68px;font-size:2.3px">Heading 04</div>
  <div class="w" style="left:116px;top:77px;font-size:2.3px">Heading 05</div>
  <div class="w" style="left:116px;top:86px;font-size:2.3px">Heading 06</div>
  <div class="w" style="left:116px;top:107px;font-size:2.3px">Heading 07</div>
  <div style="left:196px;top:31px;font-size:3.6px;font-weight:600">YOUR DATA 01<div class="tiny" style="position:static;width:40px;color:var(--ink)">Site search and early land review</div></div>
  <div style="left:183px;top:50px;font-size:3.6px;font-weight:600">YOUR DATA 03<div class="tiny" style="position:static;width:46px;color:var(--ink)">Zoning, permits and design approval</div></div>
  <div style="left:170px;top:70px;font-size:3.6px;font-weight:600">YOUR DATA 05<div class="tiny" style="position:static;width:46px;color:var(--ink)">Construction and quality checks</div></div>
  <div style="left:160px;top:101px;font-size:3.6px;font-weight:600">YOUR DATA 07<div class="tiny" style="position:static;width:46px;color:var(--ink)">Lease up and long term management</div></div>
  <div style="left:10px;top:38px;width:59px;text-align:right;font-size:3.6px;font-weight:600">YOUR DATA 02<div class="tiny" style="position:static;color:var(--ink)">Market study and rent analysis</div></div>
  <div style="left:14px;top:58px;width:59px;text-align:right;font-size:3.6px;font-weight:600">YOUR DATA 04<div class="tiny" style="position:static;color:var(--ink)">Capital plan and partner funding</div></div>
  <div style="left:26px;top:78px;width:59px;text-align:right;font-size:3.6px;font-weight:600">YOUR DATA 06<div class="tiny" style="position:static;color:var(--ink)">Final fit out and resident services</div></div>
  <div class="logo" style="left:15px;top:127px;font-size:6px;color:var(--navy)">Fernvale</div>
  <div class="pnum">15</div>
</section>

<!-- Row 6 -->
<section class="slide" style="left:8px;top:873px">
  <div class="bracket" style="left:0;top:0"></div>
  <div class="title" style="left:10px;top:6px">Our Services</div>
  <div class="ph" role="img" aria-label="Modern ceiling architecture photo" style="left:0;top:31px;width:62px;height:89px;background:linear-gradient(170deg,#e1e4e7,#3a3f44)"></div>
  <div class="ph" role="img" aria-label="Textured wall photo" style="left:62px;top:31px;width:62px;height:89px;background:linear-gradient(170deg,#cfcfcf,#8a8d90)"></div>
  <div class="ph" role="img" aria-label="Dark facade photo" style="left:124px;top:31px;width:62px;height:89px;background:linear-gradient(170deg,#3d4753,#161c23)"></div>
  <div class="ph" role="img" aria-label="Showroom building photo" style="left:186px;top:31px;width:59px;height:89px;background:linear-gradient(170deg,#c3ccd3,#2a3036)"></div>
  <div class="w" style="left:8px;top:90px;font-size:4.4px;font-weight:600">Buy Property</div>
  <div class="w" style="left:70px;top:90px;font-size:4.4px;font-weight:600">Investment Advice</div>
  <div class="w" style="left:130px;top:90px;font-size:4.4px;font-weight:600">Sell Property</div>
  <div class="w" style="left:192px;top:90px;font-size:4.4px;font-weight:600">Rental Service</div>
  <div class="tiny w" style="left:8px;top:97px;width:50px">Find homes that match your goals</div>
  <div class="tiny w" style="left:70px;top:97px;width:50px">Clear guidance on every deal</div>
  <div class="tiny w" style="left:130px;top:97px;width:50px">Reach buyers fast and fairly</div>
  <div class="tiny w" style="left:192px;top:97px;width:50px">Leasing handled from start to end</div>
  <div style="left:42px;top:112px;font-size:11px;font-weight:700;color:#cfd3d7">01</div>
  <div style="left:104px;top:112px;font-size:11px;font-weight:700;color:#cfd3d7">02</div>
  <div style="left:166px;top:112px;font-size:11px;font-weight:700;color:#cfd3d7">03</div>
  <div style="left:228px;top:112px;font-size:11px;font-weight:700;color:#cfd3d7">04</div>
  <div class="logo" style="left:15px;top:127px;font-size:6px;color:var(--navy)">Fernvale</div>
  <div class="pnum">17</div>
</section>

<section class="slide" style="left:259px;top:873px">
  <div class="bracket" style="left:0;top:0"></div>
  <div class="title" style="left:10px;top:6px">Your Title Goes Here</div>
  <div class="tiny" style="left:13px;top:28px;width:95px;font-size:3px">Occupancy across our communities has grown steadily as demand for new single family rentals keeps climbing.</div>
  <div class="ph sky" role="img" aria-label="Glass building photo" style="left:0;top:66px;width:98px;height:72px;background:linear-gradient(160deg,#5f86a8,#e3e8ec)"></div>
  <div style="left:19px;top:80px;font-size:14px;font-weight:700;color:var(--navy)">96%</div>
  <div style="left:19px;top:101px;font-size:4.5px;color:var(--navy)">Sample Text Here</div>
  <div class="tiny" style="left:19px;top:108px;width:75px;color:#3a4550">Average yearly occupancy across all of our properties</div>
  <div class="navy" style="left:98px;top:66px;width:147px;height:72px"></div>
  <svg style="left:120px;top:36px" width="118" height="100" viewBox="0 0 118 100">
    <g fill="#8d97a3" font-size="2.4" font-family="Fira Sans,sans-serif">
      <text x="0" y="5">$10.00</text><text x="0" y="19">$8.00</text><text x="0" y="33">$6.00</text><text x="0" y="47">$4.00</text><text x="0" y="61">$2.00</text><text x="0" y="75">$0.00</text>
      <text x="12" y="81">Jan</text><text x="20" y="81">Feb</text><text x="28" y="81">Mar</text><text x="36" y="81">Apr</text><text x="44" y="81">May</text><text x="52" y="81">Jun</text><text x="60" y="81">Jul</text><text x="68" y="81">Aug</text><text x="76" y="81">Sep</text><text x="84" y="81">Oct</text><text x="92" y="81">Nov</text><text x="100" y="81">Dec</text>
    </g>
    <polyline fill="none" stroke="#7d9bb0" stroke-width=".8" points="12,62 18,45 24,58 30,40 36,50 42,34 48,44 54,36 60,42 66,30 72,20 78,32 84,38 90,26 96,40 104,12"/>
    <rect x="48" y="0" width="22" height="10" fill="#fff"/>
  </svg>
  <div style="left:170px;top:38px;font-size:5px">96% <span style="position:static;font-size:2px">Title text</span></div>
</section>

<section class="slide" style="left:511px;top:873px">
  <div class="ph sky" role="img" aria-label="Sky and building background photo" style="left:0;top:0;width:245px;height:138px;background:linear-gradient(120deg,#dde3e9,#b4bcc4 60%,#f1f2f3)"></div>
  <div class="bracket" style="left:0;top:0"></div>
  <div class="title" style="left:10px;top:6px">Pring Plan</div>
  <div style="left:30px;top:25px;width:188px;height:103px;background:#fff"></div>
  <div style="left:93px;top:25px;height:103px;border-left:.4px solid #d3d7db"></div>
  <div style="left:156px;top:25px;height:103px;border-left:.4px solid #d3d7db"></div>
  <div style="left:30px;top:32px;width:63px;text-align:center;font-size:5px;font-weight:600">Start Plan<div class="tiny" style="position:static">per month</div></div>
  <div style="left:93px;top:32px;width:63px;text-align:center;font-size:5px;font-weight:600">Reguler Plan<div class="tiny" style="position:static">per month</div></div>
  <div style="left:156px;top:32px;width:62px;text-align:center;font-size:5px;font-weight:600">Premium Plan<div class="tiny" style="position:static">per month</div></div>
  <div class="navy w" style="left:30px;top:48px;width:63px;height:12px;display:flex;align-items:center;justify-content:center;font-size:7px;font-weight:600">Free</div>
  <div class="w" style="left:93px;top:48px;width:63px;height:12px;display:flex;align-items:center;justify-content:center;font-size:7px;font-weight:600;background:var(--gray)">$34</div>
  <div class="w" style="left:156px;top:48px;width:62px;height:12px;display:flex;align-items:center;justify-content:center;font-size:7px;font-weight:600;background:var(--slate)">$89</div>
  <div class="tiny" style="left:37px;top:66px;width:52px;line-height:2.7">• Site review<br>• Rent study<br>• Basic design plan<br>• Email support<br>• Monthly report</div>
  <div class="tiny" style="left:100px;top:66px;width:52px;line-height:2.7">• Site review<br>• Rent study<br>• Full design plan<br>• Phone support<br>• Weekly report</div>
  <div class="tiny" style="left:163px;top:66px;width:52px;line-height:2.7">• Site review<br>• Rent study<br>• Full design plan<br>• Priority support<br>• Daily report</div>
  <div class="btn navy" style="left:41px;top:113px;width:40px;height:9px">READ MORE</div>
  <div class="btn" style="left:104px;top:113px;width:40px;height:9px;background:var(--gray)">READ MORE</div>
  <div class="btn" style="left:167px;top:113px;width:40px;height:9px;background:var(--slate)">READ MORE</div>
  <div class="logo" style="left:15px;top:127px;font-size:6px;color:var(--navy)">Fernvale</div>
</section>

<!-- Row 7 -->
<section class="slide" style="left:8px;top:1044px">
  <div class="navy" style="left:0;top:0;width:95px;height:138px"></div>
  <div style="left:17px;top:30px;width:48px;height:86px;border-radius:7px;background:#2b3440"></div>
  <div class="ph sky" role="img" aria-label="Phone screen showing tower photo" style="left:19px;top:32px;width:44px;height:82px;border-radius:5px"></div>
  <div style="left:71px;top:20px;width:48px;height:86px;border-radius:7px;background:#2b3440"></div>
  <div class="ph sky" role="img" aria-label="Phone screen showing tower photo" style="left:73px;top:22px;width:44px;height:82px;border-radius:5px;background:linear-gradient(160deg,#e6ecf1,#4f7597)"></div>
  <div class="bracket" style="left:137px;top:26px"></div>
  <div class="title" style="left:147px;top:32px">Our Mock Up</div>
  <div class="tiny" style="left:137px;top:65px;width:82px;font-size:3px">Our pitch materials are built for every screen so partners can review each project on the go.</div>
  <div class="stat" style="left:140px;top:100px">1200k</div>
  <div class="stat" style="left:188px;top:100px">3300k</div>
  <div class="tiny" style="left:140px;top:113px;color:var(--ink)">Simple Text Here</div>
  <div class="tiny" style="left:188px;top:113px;color:var(--ink)">Simple Text Here</div>
  <div class="pnum">20</div>
</section>

<section class="slide navy" style="left:259px;top:1044px">
  <div class="bracket" style="left:0;top:0"></div>
  <div class="title w" style="left:10px;top:6px">Your Title Goes Here</div>
  <svg style="left:10px;top:32px" width="140" height="86" viewBox="0 0 140 86">
    <g fill="#8d97a3" font-size="2.6" font-family="Fira Sans,sans-serif">
      <text x="4" y="5">16</text><text x="4" y="12">14</text><text x="4" y="19">12</text><text x="4" y="26">10</text><text x="5" y="33">8</text><text x="5" y="40">6</text><text x="5" y="47">4</text><text x="5" y="54">2</text><text x="5" y="61">0</text>
      <text x="18" y="67">0</text><text x="40" y="67">2</text><text x="62" y="67">4</text><text x="84" y="67">6</text><text x="106" y="67">8</text><text x="127" y="67">10</text>
    </g>
    <polyline fill="none" stroke="#fff" stroke-width=".8" points="16,50 24,45 32,48 40,36 46,28 52,50 58,45 64,30 70,38 76,52 82,34 88,38 94,30 100,50 106,44 112,40 118,38 124,44 130,25 136,2"/>
    <rect x="60" y="23" width="16" height="10" fill="#fff"/>
    <text x="63" y="29" font-size="4" font-weight="700" fill="#131f2e" font-family="Fira Sans,sans-serif">$120</text>
  </svg>
  <div style="left:177px;top:8px;width:58px;height:54px;background:#fff"></div>
  <div style="left:177px;top:65px;width:58px;height:60px;background:#fff"></div>
  <svg style="left:193px;top:14px" width="26" height="26" viewBox="0 0 26 26">
    <circle cx="13" cy="13" r="10" fill="none" stroke="#e3e6e9" stroke-width="2"/>
    <circle cx="13" cy="13" r="10" fill="none" stroke="var(--navy)" stroke-width="2" stroke-dasharray="39 63" transform="rotate(-90 13 13)"/>
    <text x="13" y="15" font-size="5" text-anchor="middle" font-weight="700" fill="#131f2e" font-family="Fira Sans,sans-serif">62</text>
  </svg>
  <svg style="left:193px;top:72px" width="26" height="26" viewBox="0 0 26 26">
    <circle cx="13" cy="13" r="10" fill="none" stroke="#c6ccd1" stroke-width="2"/>
    <text x="13" y="15" font-size="5" text-anchor="middle" font-weight="700" fill="#6b737b" font-family="Fira Sans,sans-serif">85</text>
  </svg>
  <div class="tiny" style="left:177px;top:43px;width:58px;text-align:center;color:var(--ink)">Tittle text here</div>
  <div class="tiny" style="left:177px;top:101px;width:58px;text-align:center;color:var(--ink)">Option three</div>
  <div class="btn navy" style="left:187px;top:51px;width:38px;height:6px">READ MORE</div>
  <div class="btn" style="left:187px;top:114px;width:38px;height:6px;background:var(--slate)">READ MORE</div>
  <div style="left:0;top:121px;width:245px;height:17px;background:#fff"></div>
  <div class="logo" style="left:15px;top:127px;font-size:6px;color:var(--navy)">Fernvale</div>
  <div class="pnum">21</div>
</section>

<section class="slide" style="left:511px;top:1044px">
  <div style="left:7px;top:16px;font-size:22px;font-weight:700;color:var(--navy)">Thank’s</div>
  <div class="ph crowd" role="img" aria-label="Team celebration group photo" style="left:4px;top:53px;width:238px;height:81px"></div>
  <div class="navy" style="left:127px;top:9px;width:112px;height:36px"></div>
  <div style="left:127px;top:45px;width:112px;height:8px;background:#4b5866"></div>
  <div class="w" style="left:135px;top:14px;font-size:2.6px;line-height:1.5">Harbor Office Group<br>address 5678, USA</div>
  <div class="w" style="left:135px;top:28px;font-size:2.6px">+0000 1200 4455</div>
  <div class="w" style="left:196px;top:16px;font-size:2.6px">hello@fernvale.example</div>
  <div class="w" style="left:196px;top:28px;font-size:2.6px">www.fernvale.example</div>
  <div style="left:130px;top:16px;width:2px;height:2px;background:#fff"></div>
  <div style="left:130px;top:28px;width:2px;height:2px;background:#fff"></div>
  <div style="left:191px;top:16px;width:2px;height:2px;background:#fff"></div>
  <div style="left:191px;top:28px;width:2px;height:2px;border-radius:50%;background:#fff"></div>
  <div class="tiny w" style="left:140px;top:47px">Contact Us</div>
  <svg style="left:220px;top:47px" width="12" height="4" viewBox="0 0 12 4"><path d="M0 2H11M9 .5L11 2 9 3.5" stroke="#fff" stroke-width=".4" fill="none"/></svg>
</section>

</body>
</html>
```